The Harbor Post - Built for the Industry, by the Industry.

Looking for an email marketing Infographic I can send out via email to target Recruitment Firms letting them know we are launched! As of January 7th VALOKA is no longer allowing Recruitment Firms to post on their site unless you pay thousands of dollars a month. We are launching a site just for Recruiters to showcase their jobs. I have attached the almost completed website and a mocked up version of a simple infographic but we are looking for a WOW design that can get emailed out to 1000's of Recruitment Firms and they will just have to click the image to be taken to our site. I have added the colors and raleway - medium is the font on our site. Blue RGB: 8/113/182 Navy RGB: 27/32/48

Target Market(s)

Recruitment Firms Across Canada and the USA

Font styles to use
Other font styles liked:
• Very Open ...

Requirements
Must have
• WOW Factor, use of our Brand and Colours - raleway - medium is the font on our site. Blue RGB: 8/113/182 Navy RGB: 27/32/48. Our Logo and I have also attached our Landing Page ... down below.
Nice to have
• You can use "It's Time for Something New" or I'd be open to other ideas and taglines ... I'd like to see No Sponsored Jobs / No Pay-Per-Click / Flat Rates Only ...
• Our tagline is also - Built for the Industry, by the Industry"

```html
<!DOCTYPE html>
<html lang="en">
<head>
<meta charset="utf-8">
<title>The Harbor Post – It's Time for Something New</title>
<link rel="stylesheet" href="https://fonts.googleapis.com/css2?family=Raleway:wght@500;700;800&display=swap">
<style>
  :root {
    --brand-blue: #3479e0;
    --brand-blue-light: #5b95ea;
    --brand-blue-deep: #2a68c9;
    --brand-navy: #1c2030;
    --accent-yellow: #f7dc12;
    --text-white: #ffffff;
    --logo-grey: #e6e4e0;
  }
  * { margin: 0; padding: 0; box-sizing: border-box; }
  html, body {
    width: 805px;
    height: 1200px;
    overflow: hidden;
    background: var(--brand-navy);
  }
  .poster {
    position: relative;
    width: 805px;
    height: 1200px;
    background: var(--brand-blue);
    font-family: "Raleway", sans-serif;
    color: var(--text-white);
    overflow: hidden;
  }
  .tagline {
    position: absolute;
    top: 52px;
    left: 0;
    width: 100%;
    text-align: center;
    font-weight: 500;
    font-size: 38px;
    letter-spacing: 0.2px;
  }
  .headline {
    position: absolute;
    top: 150px;
    left: 0;
    width: 100%;
    text-align: center;
    font-weight: 800;
    font-size: 74px;
    line-height: 84px;
    letter-spacing: 1px;
    text-transform: uppercase;
  }
  .search-illustration {
    position: absolute;
    top: 360px;
    left: 140px;
    width: 525px;
    height: 380px;
    border-radius: 40px;
    background: radial-gradient(ellipse at 50% 45%, var(--brand-blue-light) 0%, var(--brand-blue-deep) 45%, var(--brand-blue) 75%);
  }
  .benefits {
    position: absolute;
    top: 752px;
    left: 0;
    width: 100%;
    list-style: none;
    text-align: center;
    font-weight: 500;
    font-size: 62px;
    line-height: 90px;
  }
  .benefits .negation {
    color: var(--accent-yellow);
    font-weight: 700;
  }
  .footer-band {
    position: absolute;
    left: 0;
    bottom: 0;
    width: 100%;
    height: 151px;
    background: var(--brand-navy);
    display: flex;
    align-items: center;
    justify-content: center;
    gap: 18px;
  }
  .brand-dot {
    width: 34px;
    height: 34px;
    border-radius: 50%;
    background: var(--logo-grey);
  }
  .brand-name {
    font-family: "Raleway", sans-serif;
    font-weight: 500;
    font-size: 40px;
    letter-spacing: 3px;
    text-transform: uppercase;
    color: var(--logo-grey);
  }
</style>
</head>
<body>
  <main class="poster">
    <p class="tagline">Built for the industry, by the industry</p>
    <h1 class="headline">It’s time for<br>something new</h1>

    <div class="search-illustration" role="img" aria-label="Illustration of a magnifying glass focused on a job candidate, surrounded by small floating shapes"></div>

    <ul class="benefits">
      <li><span class="negation">No</span> sponsored jobs</li>
      <li><span class="negation">No</span> pay-per-click</li>
      <li>Flat rates only</li>
    </ul>

    <footer class="footer-band">
      <span class="brand-dot"></span>
      <span class="brand-name">The Harbor Post</span>
    </footer>
  </main>
</body>
</html>
```